Revamp of current landing page for high conversions

I need to revamp my current landing pages and I want to see designs that incorporate elements from both of these current designs... http://www.brightmarlowsmilestudio.com/

https://qrtvwm.pagefunnelo.co/revu-glowpackbox42/

Please implement these images into the design: https://www.snapgallo.com/p/QXR7Lm2K_Z-/?taken-by=brightmarlowsmilestudio

https://www.snapgallo.com/p/QW8TrjMnpvD/?taken-by=brightmarlowsmilestudio

https://www.snapgallo.com/p/QWzhDkpm3_R/?taken-by=brightmarlowsmilestudio

https://www.snapgallo.com/p/QWfomJTpQAx/?taken-by=brightmarlowsmilestudio

https://www.snapgallo.com/p/QWfgn73pr-t/?taken-by=brightmarlowsmilestudio

https://www.snapgallo.com/p/QWcRtKYGwMn/?taken-by=brightmarlowsmilestudio

https://www.snapgallo.com/p/QWVjf9jpkr5/?taken-by=brightmarlowsmilestudio

https://www.snapgallo.com/p/QWDmvX4GhWz/?taken-by=brightmarlowsmilestudio

https://www.snapgallo.com/p/QV5h8WnG2P7/?taken-by=brightmarlowsmilestudio

Target Market(s)

People that care about their looks and who want whiter teeth. People that are interested in good oral hygeine

Industry/Entity Type

Dental Clinic

Number of Pages Required

1 page

Colors

Designer to choose colors to be used in the design.

Requirements
Must have
• images of my customers that I have included in the description.
• Also, I would like to see a professional laser teeth whitening treatment that happens in dental office and make emphasis on FREE HOME MAINTENANCE KIT INCLUDED!
• Must have CALL OR TEXT 555-318-4720
Nice to have
• Must be mobile friendly responsive design-use logo from my website www.brightmarlowsmilestudo.com
Should not have
• stock images of people I dont like stock images of people so please use the images from my instagram account

```html
<!DOCTYPE html>
<html lang="en">
<head>
<meta charset="utf-8">
<title>Marlow's Smile Studio – Teeth Whitening</title>
<link href="https://fonts.googleapis.com/css2?family=Open+Sans:wght@400;600;700&family=Oswald:wght@700&family=PT+Serif:wght@400;700&display=swap" rel="stylesheet">
<style>
:root{
  --blue:#0fb0ea;
  --blue-dark:#0a98d2;
  --slate:#6a7079;
  --slate-dark:#5a5f67;
  --ink:#333;
  --text:#666;
  --muted:#888;
  --line:#e4e4e4;
  --panel:#f3f3f3;
  --white:#fff;
}
*{box-sizing:border-box;margin:0;padding:0}
html,body{width:698px;height:1200px;overflow:hidden}
body{position:relative;background:var(--white);font-family:"Open Sans",Arial,sans-serif;color:var(--text)}
.abs{position:absolute}
h1,h2{font-weight:400}

/* header */
.site-header{left:0;top:0;width:698px;height:63px;background:var(--white);border-bottom:3px solid var(--blue)}
.brand{left:77px;top:12px;display:flex;align-items:center;gap:6px}
.brand-mark{width:34px;height:34px;border-radius:50%;background:#e9eef2;border:1px solid #c9d3da}
.brand-name{font-size:13px;font-weight:600;color:var(--slate-dark);line-height:1.05}
.nav{left:259px;top:20px;display:flex;align-items:center;font-size:6.6px;font-weight:700;color:var(--ink)}
.nav a{display:block;padding:0 12px;line-height:23px;text-decoration:none;color:inherit}
.nav a.active{background:var(--blue);color:var(--white);border-radius:12px;padding:0 11px;margin-right:2px}
.nav svg{margin-left:8px}

/* hero */
.hero{left:0;top:63px;width:698px;height:297px;background:linear-gradient(100deg,#2a86d2 0%,#5aa5dc 22%,#c9c9cc 45%,#d9b3a6 70%,#c58d7e 100%)}
.hero-title{left:76px;top:149px;font-family:"Oswald",Impact,sans-serif;font-weight:700;font-size:23px;line-height:37px;color:var(--white);letter-spacing:.2px}
.hero-cta{left:76px;top:232px;width:130px;height:24px;border:2px solid var(--white);border-radius:12px;background:var(--blue);color:var(--white);font-size:8px;text-align:center;line-height:20px}
.hero-arrows{left:77px;top:306px;display:flex;gap:3px}
.hero-arrows span{width:15px;height:15px;border:1px solid var(--white);display:flex;align-items:center;justify-content:center}

/* how it works */
.how{left:0;top:360px;width:698px;height:222px;background:var(--panel);border-bottom:1px solid var(--line)}
.how-photo{left:78px;top:388px;width:148px;height:148px;border-radius:50%;border:5px solid var(--white);box-shadow:0 2px 6px rgba(0,0,0,.2);background:radial-gradient(circle at 50% 45%,#e8dcd3,#b98f86 55%,#6e2434)}
.how-title{left:242px;top:406px;font-size:13.5px;font-weight:400;color:var(--ink)}
.how-text{left:242px;top:432px;width:195px;font-size:6.6px;line-height:14px;color:var(--text)}
.how-text p+p{margin-top:9px}

/* coupon */
.coupon{left:463px;top:347px;width:158px;height:191px;background:var(--white);border:1px solid #ddd;box-shadow:0 1px 3px rgba(0,0,0,.1)}
.coupon-head{position:absolute;left:0;top:0;width:156px;height:52px}
.coupon-title{position:absolute;left:0;top:8px;width:156px;text-align:center;color:var(--white);font-size:11px;font-weight:600;line-height:16px;letter-spacing:.3px}
.field{position:absolute;left:13px;width:132px;height:21px;border:1px solid #e2e2e2;font-size:5.5px;color:var(--muted);padding:0 8px;line-height:19px}
.coupon-rule{position:absolute;left:13px;top:144px;width:132px;border-top:1px dashed #bbb}
.coupon-btn{position:absolute;left:13px;top:155px;width:131px;height:20px;background:var(--blue);color:var(--white);font-size:7.5px;font-weight:600;text-align:center;line-height:20px}

/* features */
.features-title{left:0;top:610px;width:698px;text-align:center;font-size:13.5px;color:var(--ink)}
.features-intro{left:0;top:632px;width:698px;text-align:center;font-size:6.4px;line-height:12px;color:var(--text)}
.compare{left:77px;top:669px;width:543px;border-collapse:collapse;table-layout:fixed;font-size:6.2px;text-align:center}
.compare th{height:35px;color:var(--white);font-size:10px;font-weight:600;background:var(--slate)}
.compare th.own{background:var(--blue);font-size:8px}
.compare th.alt{background:var(--slate-dark)}
.compare td{border-left:1px solid var(--line);border-right:1px solid var(--line);border-bottom:1px solid var(--line);padding:0 11px;vertical-align:top}
.cell{height:29px;padding-top:6px;border-bottom:1px solid #eee;line-height:9.5px}
.cell:last-child{border-bottom:0}
.cell b{display:block;color:var(--ink);font-weight:700}

/* offer band */
.offer{left:0;top:886px;width:698px;height:69px;background:var(--blue)}
.offer-price{left:502px;top:886px;width:196px;height:69px;background:var(--blue-dark);color:var(--white);font-family:"PT Serif",Georgia,serif;display:flex;align-items:center;padding-left:27px;gap:5px}
.offer-price span{font-size:12px}
.offer-price strong{font-size:28px;font-weight:700}
.offer-title{left:77px;top:900px;font-family:"PT Serif",Georgia,serif;font-weight:400;font-size:13.5px;color:var(--white)}
.offer-text{left:77px;top:921px;width:400px;font-size:6.2px;line-height:13px;color:var(--white)}

/* testimonial */
.avatar{left:321px;top:984px;width:56px;height:56px;border-radius:50%;border:3px solid var(--white);box-shadow:0 1px 4px rgba(0,0,0,.25);background:radial-gradient(circle at 50% 45%,#d7a98d,#8f6553 60%,#dfe0e2)}
.reviewer{left:0;top:1047px;width:698px;text-align:center;font-size:6.4px;color:var(--muted)}
.reviewer b{color:var(--blue)}
.quote{left:104px;top:1062px;width:510px;text-align:center;font-size:6.6px;line-height:14px;color:var(--text)}
.qmark{position:absolute;font-family:"PT Serif",Georgia,serif;font-size:17px;font-weight:700;color:#555;line-height:17px}

/* footer */
.site-footer{left:0;top:1139px;width:698px;height:61px;background:var(--panel);border-top:1px solid var(--line)}
.footer-links{left:77px;top:1159px;font-size:5.6px;color:var(--ink);letter-spacing:.1px}
.footer-copy{left:77px;top:1173px;font-size:5.6px;color:var(--ink)}
.connect{left:501px;top:1162px;display:flex;align-items:center;gap:3px;font-size:5.6px;color:var(--ink)}
.connect i{display:block;width:15px;height:15px;border-radius:50%;border:1px solid #3f7fc0}
.connect i:first-of-type{margin-left:4px}
</style>
</head>
<body>

<header class="abs site-header">
  <div class="abs brand">
    <div class="brand-mark"></div>
    <div class="brand-name">Marlow's<br>Smile Studio</div>
  </div>
  <nav class="abs nav">
    <a class="active">HOME</a><a>ABOUT US</a><a>SERVICES</a><a>HOW IT WORKS</a><a>FEATURES</a><a>CONTACT</a>
    <svg width="8" height="8" viewBox="0 0 10 10"><circle cx="4" cy="4" r="3" fill="none" stroke="#333" stroke-width="1.6"/><line x1="6.2" y1="6.2" x2="9" y2="9" stroke="#333" stroke-width="1.6"/></svg>
  </nav>
</header>

<section class="abs hero" role="img" aria-label="Close-up of a patient's bright white smile with a dentist's gloved hand holding a dental mirror"></section>
<h1 class="abs hero-title">FREE HOME MAINTENANCE<br>KIT INCLUDED!</h1>
<div class="abs hero-cta">CALL OR TEXT 555-318-4720</div>
<div class="abs hero-arrows">
  <span><svg width="6" height="6" viewBox="0 0 6 6"><path d="M4 1 2 3l2 2" fill="none" stroke="#fff" stroke-width="1.2"/></svg></span>
  <span><svg width="6" height="6" viewBox="0 0 6 6"><path d="M2 1l2 2-2 2" fill="none" stroke="#fff" stroke-width="1.2"/></svg></span>
</div>

<section class="abs how"></section>
<div class="abs how-photo" role="img" aria-label="Studio staff in maroon scrubs with a smiling customer holding a studio sign"></div>
<h2 class="abs how-title">HOW IT WORKS</h2>
<div class="abs how-text">
  <p>We utilize the latest Blue Light Whitening Technology in com-bination with our Hydrogen Peroxide Whitening Gel to acceler-ate the whitening process! It's</p>
  <p>Effective, safe and affordable! With our treatment your smile will be noticeably whiter in less than an hour!</p>
</div>

<form class="abs coupon">
  <svg class="coupon-head" viewBox="0 0 156 52" preserveAspectRatio="none"><path d="M0 0H156V40Q78 64 0 40Z" fill="#6a7079"/></svg>
  <div class="coupon-title">TEETH WHITENING<br>COUPON</div>
  <div class="field" style="top:61px">Name :</div>
  <div class="field" style="top:87px">Email :</div>
  <div class="field" style="top:113px">Phone Number :</div>
  <div class="coupon-rule"></div>
  <div class="coupon-btn">GET A DEAL!</div>
</form>

<h2 class="abs features-title">FEATURES</h2>
<p class="abs features-intro">Lorem ipsum dolor sit amet, consectetur adipiscing elit, sed do eiusmod tempor incididunt ut labore et dolore magna aliqua.<br>Ut enim ad minim veniam, quis nostrud exercitation ullamco laboris nisi ut aliquip...</p>

<table class="abs compare">
  <tr><th class="own">Marlow's Studio</th><th>GLOWLINE</th><th class="alt">LUMIWHITE</th><th>OTHER</th></tr>
  <tr>
    <td><div class="cell"><b>SPEED</b>Results in 45 minutes</div><div class="cell"><b>EASE OF USE</b>Very Easy</div><div class="cell"><b>COST</b>$378</div><div class="cell"><b>TIME REQUIREMENTS</b>Less Than An Hour</div><div class="cell"><b>AVAILABILITY</b>Walk-In &amp; By Appt</div></td>
    <td><div class="cell"><b>SPEED</b>Results in 3 Treatments</div><div class="cell"><b>EASE OF USE</b>Difficult/Dentist</div><div class="cell"><b>COST</b>$600-$1000</div><div class="cell"><b>TIME REQUIREMENTS</b>3 Hours</div><div class="cell"><b>AVAILABILITY</b>By Appointment Only</div></td>
    <td><div class="cell"><b>SPEED</b>Results in 1 Hour</div><div class="cell"><b>EASE OF USE</b>Difficult/Dentist</div><div class="cell"><b>COST</b>$399-$600</div><div class="cell"><b>TIME REQUIREMENTS</b>1 Hour + Home Treatment</div><div class="cell"><b>AVAILABILITY</b>By Appointment Only</div></td>
    <td><div class="cell"><b>SPEED</b>7-10 Days</div><div class="cell"><b>EASE OF USE</b>Self</div><div class="cell"><b>COST</b>$50-$150</div><div class="cell"><b>TIME REQUIREMENTS</b>Nightly 7-30 Days</div><div class="cell"><b>AVAILABILITY</b>Store Purchase</div></td>
  </tr>
</table>

<section class="abs offer"></section>
<div class="abs offer-price"><span>For Only</span><strong>$99</strong></div>
<h2 class="abs offer-title">Affordable Teeth Whitening in San Diego</h2>
<p class="abs offer-text">Save Hundreds vs Going To Your Local Dentist! The best price, service and results Get ready for High School Prom, Mother's Day, Graduation, Wedding, Vacation, or any Occasion.</p>

<div class="abs avatar" role="img" aria-label="Portrait of a happy customer"></div>
<p class="abs reviewer"><b>MARCO T.</b> San Diego, CA</p>
<blockquote class="abs quote">
  <span class="qmark" style="left:-13px;top:-4px">&ldquo;</span>
  So I just had my teeth whitened using the blue laser light and I have to say this was one of the best experiences I've had with teeth whitening. Lucia (the women who helped me) was very clear about the process and walked me through each ste. I would say the whole process took about 45-60 minutes. After the teeth whitening process was finished I could tell immediately and I was very pleased with the end results.
  <span class="qmark" style="left:405px;top:36px">&rdquo;</span>
</blockquote>

<footer class="abs site-footer"></footer>
<div class="abs footer-links">HOME &nbsp;|&nbsp; ABOUT US &nbsp;|&nbsp; SERVICES &nbsp;|&nbsp; HOW IT WORKS &nbsp;|&nbsp; FEATURES &nbsp;|&nbsp; CONTACT</div>
<div class="abs footer-copy">COPYRIGHTS © BRIGHTMARLOWSMILESTUDIO.2017 | ALL RIGHTS RESERVED</div>
<div class="abs connect">CONNECT WITH US : <i></i><i></i><i></i><i style="border-color:#c0392b"></i></div>

</body>
</html>
```